UPLIFT Group Fitness Class Launch Poster!

We need a poster design for a upcoming Group Fitness Class launch with two additional social media post designs.
Please follow our Brand Style Guide, as I will not be able to accept anything outside of this guide.
Class Description:
Come and UPLIFT your body with this class while catching up with friends and meeting new people. It is low-impact strength training with bodyweight exercises to help improve muscular strength, cardiovascular endurance, balance, bone health and functional training. It is suitable for all fitness levels.
Class Length: 30 Minutes
Intro script for class online:
📣New class alert❗
PWL team is excited to announce the launch of our new class, "UPLIFT", instructed by Jo! 🥰
Unsure if group fitness classes are for you? Join us for 30-minute low-impact strength training with bodyweight exercises! It's time to build your confidence in a fun and supportive environment.
Target Market(s)
Target audience is mostly females which barrier to entry to fitness is not having the confidence to join or has limited capability and needing low impact. Important to note that our demographic tends to be below 50... So barriers is most likely to be confidence, overweight or unfit.
Industry/Entity Type
Fitness
Font styles to use
Other font styles liked:
- Please follow the Style Guide Fonts.
Requirements
Must have
- The project must follow our Brand Guidelines & include the class logo. Poster should be exciting and stand out. Don't necessarily have to use the stock images provided.
Should not have
- If you select your own image, the preference would be that it does not only include slim/fit looking individuals.

```html
<!DOCTYPE html>
<html lang="en">
<head>
<meta charset="utf-8">
<title>UPLIFT Class Launch – Poster and Social Posts</title>
<link href="https://fonts.googleapis.com/css2?family=Outfit:wght@400;500;600;700;800;900&display=swap" rel="stylesheet">
<style>
  :root{
    --stage:#e6e7e8;
    --black:#121212;
    --red:#e0262f;
    --crimson:#c8273a;
    --badge:#e9e9ea;
    --white:#ffffff;
    --text-dark:#333333;
    --frame:#8a8a8a;
  }
  *{box-sizing:border-box;margin:0;padding:0}
  html,body{width:1200px;height:754px;overflow:hidden;background:var(--stage);font-family:'Outfit',sans-serif}
  .canvas{position:relative;width:1200px;height:754px;background:var(--stage)}

  .poster{position:absolute;left:3px;top:0;width:538px;height:754px;background:var(--black);overflow:hidden;color:var(--white)}
  .poster-art{position:absolute;inset:0}
  .brand{position:absolute;left:50px;top:340px;display:flex;align-items:center;gap:6px;font-weight:700;font-size:14px;color:var(--white);white-space:nowrap}
  .brand-dot{width:10px;height:10px;border-radius:50%;background:var(--white)}
  .duration-number{position:absolute;left:196px;width:150px;top:296px;text-align:center;font-weight:800;font-size:72px;line-height:1;color:var(--crimson);letter-spacing:-2px}
  .duration-unit{position:absolute;left:196px;width:150px;top:366px;text-align:center;font-weight:700;font-size:21px;line-height:1.1;color:#3a3a3a}
  .class-name{position:absolute;left:358px;top:332px;font-weight:900;font-size:38px;letter-spacing:1px;color:var(--white)}
  .intro{position:absolute;left:20px;right:20px;top:436px;text-align:center;font-weight:600;font-size:11px;line-height:14.5px}
  .divider{position:absolute;left:165px;top:543px;width:208px;height:14px}
  .alert-row{position:absolute;left:0;right:0;top:572px;text-align:center;font-weight:800;font-size:26px;color:var(--crimson);letter-spacing:-0.5px}
  .megaphone{position:absolute;top:555px;width:60px;height:50px;border-radius:6px;background:linear-gradient(135deg,#e9e9ea,#b8bcc0 60%,#c8273a)}
  .megaphone.left{left:88px}
  .megaphone.right{left:390px}
  .announce{position:absolute;left:0;right:0;top:611px;text-align:center;font-weight:700;font-size:10px}
  .points{position:absolute;left:51px;top:634px;display:flex}
  .point{width:163px}
  .point-title{display:flex;align-items:center;gap:6px;font-weight:800;font-size:15px}
  .point-title svg{width:22px;height:18px}
  .point-text{margin-top:7px;padding-left:4px;font-size:6.8px;line-height:9px;font-weight:500;width:108px}
  .footer{position:absolute;left:0;right:0;bottom:0;height:49px;background:linear-gradient(90deg,#8f1a22,#c8262e 55%,#7a161c);display:flex;align-items:center;justify-content:center;font-weight:500;font-size:14px;letter-spacing:1.6px;padding-bottom:12px}

  .post{position:absolute;background:var(--white);border:1px solid var(--frame);display:flex;align-items:center;justify-content:center;text-align:center;font-weight:700;font-size:20px;line-height:26px;color:var(--text-dark)}
  .post-square{left:696px;top:35px;width:348px;height:348px;align-items:flex-start;padding-top:126px}
  .post-wide{left:564px;top:400px;width:613px;height:318px}
</style>
</head>
<body>
<div class="canvas">
  <section class="poster">
    <svg class="poster-art" viewBox="0 0 538 754" width="538" height="754">
      <defs>
        <linearGradient id="photoTone" x1="0" y1="0" x2="1" y2="1">
          <stop offset="0" stop-color="#2a2d31"/>
          <stop offset="0.5" stop-color="#3b3d40"/>
          <stop offset="1" stop-color="#25282b"/>
        </linearGradient>
        <linearGradient id="stripe" x1="0" y1="0" x2="1" y2="1">
          <stop offset="0" stop-color="#f0282f"/>
          <stop offset="1" stop-color="#7e141a"/>
        </linearGradient>
      </defs>
      <polygon points="0,0 538,0 538,244 270,325 0,244" fill="url(#photoTone)" role="img" aria-label="Photo of three people doing bodyweight squats in a gym"/>
      <polygon points="0,430 95,378 80,412 0,452" fill="url(#stripe)"/>
      <polygon points="0,485 153,396 130,446 0,510" fill="url(#stripe)"/>
      <polygon points="170,438 225,395 250,408 195,432" fill="url(#stripe)"/>
      <polygon points="318,400 362,412 372,436 330,420" fill="url(#stripe)"/>
      <polygon points="393,396 538,470 538,510 430,460" fill="url(#stripe)"/>
      <circle class="duration-badge" cx="271" cy="348" r="74" fill="var(--badge)"/>
    </svg>

    <div class="brand"><span class="brand-dot"></span>Northridge Shire</div>
    <div class="duration-number">30</div>
    <div class="duration-unit">Minutes</div>
    <div class="class-name">UPLIFT</div>

    <p class="intro">Come and UPLIFT your body<br>with this class while catching up with<br>friends and meeting new people.<br>It is low-impact strength training with body<br>weight exercises to help improve muscular strength,<br>cardiovascular endurance, balance, bone health and functional training.<br>It is suitable for all fitness levels.</p>

    <svg class="divider" viewBox="0 0 208 14">
      <g fill="none" stroke="#fff" stroke-width="2">
        <path d="M2 2 l5 5 -5 5 M14 2 l5 5 -5 5 M26 2 l5 5 -5 5 M38 2 l5 5 -5 5"/>
        <path d="M60 7 H146"/>
        <path d="M170 2 l-5 5 5 5 M182 2 l-5 5 5 5 M194 2 l-5 5 5 5 M206 2 l-5 5 5 5"/>
      </g>
    </svg>
    <div class="megaphone left" role="img" aria-label="Megaphone illustration"></div>
    <div class="alert-row">NEW CLASS ALERT</div>
    <div class="megaphone right" role="img" aria-label="Megaphone illustration"></div>

    <p class="announce">PWL team is excited to announce the launch of our new class, “UPLIFT”, instructed by Jo!</p>

    <div class="points">
      <div class="point">
        <div class="point-title"><svg viewBox="0 0 22 18"><path d="M2 9 l6 7 L20 2" fill="none" stroke="var(--red)" stroke-width="4"/></svg>UNSURE?</div>
        <p class="point-text">Unsure if group fitness classes are for you?</p>
      </div>
      <div class="point">
        <div class="point-title"><svg viewBox="0 0 22 18"><path d="M2 9 l6 7 L20 2" fill="none" stroke="var(--red)" stroke-width="4"/></svg>JOIN US!</div>
        <p class="point-text">Join us for 30-minute low-impact strength training with body weight exercises!</p>
      </div>
      <div class="point">
        <div class="point-title"><svg viewBox="0 0 22 18"><path d="M2 9 l6 7 L20 2" fill="none" stroke="var(--red)" stroke-width="4"/></svg>IT’S FUN!</div>
        <p class="point-text">It’s time to build your confidence in a fun and supportive environment.</p>
      </div>
    </div>

    <div class="footer">www.northridgeshire.com</div>
  </section>

  <div class="post post-square">SOCIAL MEDIA FLYER STILL<br>IN DESIGNING PROCESS!</div>
  <div class="post post-wide">SOCIAL MEDIA FLYER STILL IN DESIGNING PROCESS!</div>
</div>
</body>
</html>
```